Kestrel Building Works Business Card and more!

We need a business card design for Kestrel Building Works Ltd, a respected building company that specialises in high quality designer homes.

We're after a sleek, clean, modern business card that incorporates our new logo (see attached) and colours, with black being the background.

We are Certified Framing Guild and need to include their logo (see attached) on our cards, balancing but not taking over our logo.

Details to be included:

Malcolm Tivey
Director

Phone: 0218845126
Email: kestrelbuild.nz@maildrop-example.co.nz
Website: www.kestrelbuildingworks-example.co.nz

Additional Information

A start up website is also under construction and needing attention and letterheads are needed!

We look forward to your designs!

Target Market(s)

30+ people who are interested in building new or renovating current homes

Industry/Entity Type

Construction

Contact Information for Business Card

Malcolm Tivey
Director

Phone: 0218845126
Facebook: www.socialpage-example.com/kestrelbuild.nz

Font styles to use
Serif

Colors

Designer to choose colors to be used in the design.

Requirements
Must have
• Our new logo
• Our colours
• cfg logo

```html
<!DOCTYPE html>
<html lang="en">
<head>
<meta charset="utf-8">
<title>Kestrel Building Works – Business Card</title>
<link rel="stylesheet" href="https://fonts.googleapis.com/css2?family=Cinzel:wght@600&family=Montserrat:wght@400;600;700&display=swap">
<style>
  :root {
    --stage: #26282c;
    --card-black: #0d0d0f;
    --strip-black: #050506;
    --navy: #24324f;
    --navy-deep: #1c2841;
    --gold: #d4a872;
    --silver: #dfe3ea;
    --white: #ffffff;
    --ghost: rgba(255,255,255,0.14);
  }
  * { box-sizing: border-box; margin: 0; padding: 0; }
  html, body { width: 1200px; height: 900px; overflow: hidden; }
  body {
    background: var(--stage);
    font-family: "Montserrat", sans-serif;
    position: relative;
  }
  .card {
    position: absolute;
    top: 150px;
    width: 360px;
    height: 600px;
    border-radius: 26px;
    overflow: hidden;
    background: var(--card-black);
    box-shadow: 0 18px 40px rgba(0,0,0,0.45);
  }
  .card--details { left: 190px; }
  .card--brand { left: 650px; background: var(--navy); }
  .card-art { position: absolute; inset: 0; width: 100%; height: 100%; }

  /* details side */
  .details-mark {
    position: absolute; top: 120px; left: 0; right: 0;
    text-align: center;
    font-family: "Cinzel", serif; font-weight: 600;
    font-size: 26px; line-height: 1.2; letter-spacing: 3px;
    color: var(--ghost);
  }
  .person {
    position: absolute; top: 370px; left: 0; right: 0; text-align: center;
  }
  .person-name {
    color: var(--white); font-weight: 700; font-size: 22px; letter-spacing: 0.5px;
  }
  .person-role {
    color: var(--gold); font-size: 14px; letter-spacing: 1.5px; margin-top: 2px;
  }
  .contacts {
    position: absolute; left: 28px; bottom: 36px; list-style: none;
  }
  .contacts li {
    display: flex; align-items: center; gap: 10px;
    color: var(--white); font-size: 12.5px; margin-top: 10px;
  }
  .contacts svg { width: 16px; height: 16px; flex: none; }

  /* brand side */
  .brand-name {
    position: absolute; top: 200px; left: 0; right: 0; text-align: center;
    font-family: "Cinzel", serif; font-weight: 600;
    font-size: 38px; line-height: 1.15; letter-spacing: 4px;
    color: var(--white);
  }
  .brand-web {
    position: absolute; bottom: 32px; left: 0; right: 0; text-align: center;
    color: var(--gold); font-size: 12.5px; letter-spacing: 0.5px;
  }
</style>
</head>
<body>

<section class="card card--details" aria-label="Business card, contact side">
  <svg class="card-art" viewBox="0 0 360 600" aria-hidden="true">
    <rect x="0" y="0" width="360" height="600" fill="var(--card-black)"/>
    <rect x="0" y="0" width="360" height="44" fill="var(--strip-black)"/>
    <polygon points="0,44 360,44 360,250 180,320 0,250" fill="var(--navy)"/>
    <polyline points="0,250 180,320 360,250" fill="none" stroke="var(--silver)" stroke-width="2.5"/>
    <polygon points="170,345 190,345 180,360" fill="var(--gold)"/>
  </svg>
  <div class="details-mark">Kestrel<br>Building Works</div>
  <div class="person">
    <p class="person-name">MALCOLM TIVEY</p>
    <p class="person-role">DIRECTOR</p>
  </div>
  <ul class="contacts">
    <li>
      <svg viewBox="0 0 16 16" aria-hidden="true"><path d="M2 4c0-1 1-2 2-2h8c1 0 2 1 2 2v1h-3V4H5v1H2z M3 7h10l1 6H2z" fill="var(--gold)"/></svg>
      0218845126
    </li>
    <li>
      <svg viewBox="0 0 16 16" aria-hidden="true"><rect x="1" y="3" width="14" height="10" rx="1" fill="var(--gold)"/><polyline points="1.5,3.5 8,9 14.5,3.5" fill="none" stroke="var(--card-black)" stroke-width="1.3"/></svg>
      kestrelbuild.nz@maildrop-example.co.nz
    </li>
    <li>
      <svg viewBox="0 0 16 16" aria-hidden="true"><circle cx="8" cy="8" r="6.5" fill="none" stroke="var(--gold)" stroke-width="1.3"/><ellipse cx="8" cy="8" rx="2.8" ry="6.5" fill="none" stroke="var(--gold)" stroke-width="1.1"/><line x1="1.5" y1="8" x2="14.5" y2="8" stroke="var(--gold)" stroke-width="1.1"/></svg>
      www.kestrelbuildingworks-example.co.nz
    </li>
  </ul>
</section>

<section class="card card--brand" aria-label="Business card, brand side">
  <svg class="card-art" viewBox="0 0 360 600" aria-hidden="true">
    <rect x="0" y="0" width="360" height="600" fill="var(--navy)"/>
    <polygon points="0,500 210,500 360,430 360,600 0,600" fill="var(--card-black)"/>
    <polyline points="200,500 215,500 360,432" fill="none" stroke="var(--gold)" stroke-width="3"/>
    <rect x="165" y="525" width="30" height="3" fill="var(--gold)"/>
  </svg>
  <div class="brand-name">Kestrel<br>Building<br>Works</div>
  <p class="brand-web">www.kestrelbuildingworks-example.co.nz</p>
</section>

</body>
</html>
```